Corvath Holdings, LLC

We are a design build general contracting company.
We work with commercial accounts and private developers. We build retail spaces, restaurants and housing projects.
Im looking for a clean professional type of logo incorporating a roman flavor, think ionic columns and pedestals.
Two toned colorway.
I like unusual fonts and Im not afraid to do something bold with the logo.
Contact Information for Business Card
Marisol Brenkowitz
318-472-9051 corvathmb@mailvexo.com
Font styles to use
Decorative
Colors
Designer to choose colors to be used in the design.
Requirements
Should not have
- I don't like reds pinks.

```html
<!DOCTYPE html>
<html lang="en">
<head>
<meta charset="utf-8">
<title>Corvath Holdings, LLC — Business Card</title>
<link rel="stylesheet" href="https://fonts.googleapis.com/css2?family=Cinzel:wght@500;600&family=Work+Sans:wght@400;500&display=swap">
<style>
  :root {
    --backdrop: #2a2a2a;
    --card: #1c1c1c;
    --gold: #c9a24a;
    --ink: #f2f2f2;
  }
  * { margin: 0; padding: 0; box-sizing: border-box; }
  html, body { width: 1200px; height: 900px; overflow: hidden; }
  body {
    background: var(--backdrop);
    position: relative;
    font-family: "Work Sans", Arial, sans-serif;
  }
  .card {
    position: absolute;
    left: 250px;
    width: 700px;
    height: 400px;
    background: var(--card);
    border-bottom: 7px solid var(--gold);
    box-shadow: 0 10px 24px rgba(0,0,0,0.45);
  }
  .card--front { top: 25px; }
  .card--back { top: 470px; }

  .brand-name {
    position: absolute;
    top: 0; left: 0; right: 0; bottom: 0;
    display: flex;
    align-items: center;
    justify-content: center;
    gap: 18px;
    font-family: "Cinzel", Georgia, serif;
    font-weight: 500;
    font-size: 38px;
    letter-spacing: 1px;
    color: var(--gold);
  }
  .brand-mark {
    width: 14px; height: 14px;
    background: var(--gold);
  }

  .person {
    position: absolute;
    right: 420px;
    top: 148px;
    text-align: right;
  }
  .person-name {
    font-family: "Cinzel", Georgia, serif;
    font-weight: 600;
    font-size: 27px;
    color: var(--gold);
    white-space: nowrap;
  }
  .person-title {
    font-size: 17px;
    letter-spacing: 1px;
    color: var(--ink);
    margin-top: 2px;
  }
  .divider {
    position: absolute;
    left: 298px;
    top: 140px;
    width: 2px;
    height: 78px;
    background: var(--gold);
  }
  .contact-list {
    position: absolute;
    left: 322px;
    top: 142px;
    list-style: none;
  }
  .contact-item {
    display: flex;
    align-items: center;
    gap: 12px;
    font-size: 18px;
    line-height: 25px;
    letter-spacing: 0.5px;
    color: var(--ink);
  }
  .contact-icon { width: 13px; height: 13px; flex: none; }
  .web-domain { color: var(--gold); }
  .address {
    position: absolute;
    left: 0; right: 0;
    top: 318px;
    text-align: center;
    font-size: 18px;
    letter-spacing: 0.5px;
    color: var(--ink);
  }
</style>
</head>
<body>
  <section class="card card--front">
    <div class="brand-name"><span class="brand-mark"></span>Corvath Holdings, LLC</div>
  </section>

  <section class="card card--back">
    <div class="person">
      <div class="person-name">Marisol Brenkowitz</div>
      <div class="person-title">Director</div>
    </div>
    <div class="divider"></div>
    <ul class="contact-list">
      <li class="contact-item">
        <svg class="contact-icon" viewBox="0 0 16 16"><path fill="#c9a24a" d="M3.5 1l2.5 3-1.5 1.8c.9 2 2.5 3.6 4.5 4.5L10.8 9l3 2.5-1.3 2.8C7 14 2 9 1.5 3.2z"/></svg>
        318-472-9051
      </li>
      <li class="contact-item">
        <svg class="contact-icon" viewBox="0 0 16 16"><rect x="1" y="3" width="14" height="10" fill="none" stroke="#c9a24a" stroke-width="1.5"/><path d="M1 3l7 6 7-6" fill="none" stroke="#c9a24a" stroke-width="1.5"/></svg>
        corvathmb@mailvexo.com
      </li>
      <li class="contact-item">
        <svg class="contact-icon" viewBox="0 0 16 16"><g fill="none" stroke="#c9a24a" stroke-width="1.3"><circle cx="8" cy="8" r="6.5"/><ellipse cx="8" cy="8" rx="3" ry="6.5"/><path d="M1.5 8h13"/></g></svg>
        <span>www.<span class="web-domain">corvathholdingsllc</span>.com</span>
      </li>
    </ul>
    <p class="address">2750 Larkmoor Valley Rd Rosa, CA 95418-3307</p>
  </section>
</body>
</html>
```